Food Safety 1-California workers only

3.25" by 4.5" Black and White Magazine Ad
This ad is to train California workers only.
Workers will be trained on: Food Safety, FSMA (Food Safety Modernization Act), using equipment safety, food processing production skills, worker safety, supervisory skills, communication skills.
"FREE TRAINING", The company does the training or Keystone Learning will provide the training.
Training grants range from $100,000 to $400,000.
Companies must be in business for profit.
Companies must train 200 employees or more.
This program is for California workers only.
Incumbent or new-hires are eligible.

Target Market(s)

California food processors, farms, food packaging, food processors, companies under FSMA, food safety, food production who need to train employees.

Industry/Entity Type

Food Production

Font styles to use
Serif
Sans Serif

Colors

Designer to choose colors to be used in the design.

Requirements
Must have
• This is a 3.25 inch by 4.5 inch magazine ad. It must be black and white. No color.
• The deliverable must be in basic PhotoShop. The ad does not need to include any graphics and be text only if needed. If you have a black and white graphic that will show well.
• Look at www.KLGFoodSafety..com
• Use the text from "MEALBOX-Photoshop-052018" file as your starting point.
Nice to have
• A black and white graphic about food. See www.KLGFoodSafety.com
Should not have
• No color.

```html
<!DOCTYPE html>
<html lang="en">
<head>
<meta charset="utf-8">
<title>Keystone Learning – Free Training Ad</title>
<link rel="stylesheet" href="https://fonts.googleapis.com/css2?family=Oswald:wght@400;600;700&family=Lato:wght@400;700;900&display=swap">
<style>
  :root {
    --backdrop: #858585;
    --paper: #ffffff;
    --ink: #111111;
    --photo-dark: #3a3a3a;
    --photo-mid: #8a8a8a;
    --photo-light: #d6d6d6;
    --rule: #333333;
  }
  * { box-sizing: border-box; margin: 0; padding: 0; }
  html, body { width: 1200px; height: 1200px; overflow: hidden; background: var(--backdrop); }
  .ad {
    position: absolute; left: 240px; top: 72px; width: 746px; height: 1034px;
    background: var(--paper); overflow: hidden;
    box-shadow: 4px 6px 10px rgba(0,0,0,.35);
    font-family: "Lato", sans-serif; color: var(--ink);
  }
  .hero { position: absolute; left: 0; top: 0; width: 746px; height: 380px; }
  .headline {
    position: absolute; left: 15px; top: 272px;
    font-family: "Oswald", sans-serif; text-transform: uppercase; line-height: 1;
    white-space: nowrap;
  }
  .headline .line-one {
    display: block; font-size: 64px; font-weight: 400; letter-spacing: -.5px;
    transform: scaleX(.93); transform-origin: left center;
  }
  .headline .line-two {
    display: block; font-size: 62px; font-weight: 700; letter-spacing: -1px; margin-top: 2px;
    transform: scaleX(.86); transform-origin: left center;
  }
  .panel {
    position: absolute; left: 16px; width: 714px;
    border: 1.5px solid var(--rule); border-radius: 8px;
  }
  .panel-label {
    position: absolute; top: -19px; left: 50%; transform: translateX(-50%);
    background: var(--ink); color: var(--paper); border-radius: 14px;
    font-weight: 900; font-size: 21px; letter-spacing: .5px; white-space: nowrap;
    padding: 6px 24px; line-height: 23px;
  }
  .training { top: 451px; height: 194px; }
  .topic { position: absolute; top: 59px; width: 180px; margin-left: -90px; text-align: center; }
  .topic svg { display: block; margin: 0 auto; }
  .topic-name { margin-top: 17px; font-size: 17.5px; line-height: 23px; text-transform: uppercase; }
  .produce-wash {
    position: absolute; left: 0; top: 630px; width: 746px; height: 300px;
    background: linear-gradient(180deg, rgba(255,255,255,0) 0%, #e2e2e2 30%, #d4d4d4 70%, #eeeeee 100%);
  }
  .qualify { top: 688px; height: 222px; background: rgba(255,255,255,.35); }
  .criteria { position: absolute; list-style: none; font-size: 19px; line-height: 23px; }
  .criteria li { position: relative; }
  .criteria li::before {
    content: ""; position: absolute; left: -18px; top: 8px;
    width: 9px; height: 9px; border-radius: 50%; background: var(--ink);
  }
  .criteria b { font-weight: 700; }
  .criteria-left { left: 31px; top: 30px; width: 290px; }
  .criteria-left li { margin-bottom: 23px; }
  .criteria-right { left: 397px; top: 31px; width: 290px; }
  .criteria-right li { margin-bottom: 22px; }
  .footer-rule { position: absolute; left: 0; top: 926px; width: 746px; height: 2px; background: var(--ink); }
  .footer {
    position: absolute; left: 0; top: 932px; width: 746px; height: 102px;
    background: var(--ink); color: var(--paper); font-size: 14.5px; line-height: 19px;
  }
  .footer .address { position: absolute; left: 23px; top: 12px; font-style: normal; }
  .footer .address strong { font-weight: 700; }
  .footer .divider { position: absolute; top: 8px; width: 3px; height: 88px; background: var(--paper); }
  .contact { position: absolute; display: flex; align-items: center; gap: 9px; white-space: nowrap; }
  .contact svg { flex: none; }
  .contact-email span { font-size: 14px; letter-spacing: -.1px; }
</style>
</head>
<body>
<div class="ad">
  <svg class="hero" viewBox="0 0 746 380">
    <defs>
      <linearGradient id="plate" x1="0" y1="0" x2="1" y2="1">
        <stop offset="0" stop-color="var(--photo-mid)"/>
        <stop offset=".45" stop-color="var(--photo-dark)"/>
        <stop offset=".75" stop-color="var(--photo-light)"/>
        <stop offset="1" stop-color="var(--photo-mid)"/>
      </linearGradient>
    </defs>
    <path d="M0 0 H746 V380 C720 320 700 330 650 350 C600 250 560 250 470 215 C360 180 250 175 150 150 C70 135 20 110 0 70 Z" fill="var(--ink)"/>
    <path role="img" aria-label="Photo of a plated herb-crusted chicken dish with roasted vegetables, in black and white"
          d="M30 0 H746 V318 C720 310 690 320 660 330 C610 250 560 240 470 205 C370 170 260 160 170 135 C95 115 50 70 30 0 Z" fill="url(#plate)"/>
  </svg>

  <h1 class="headline">
    <span class="line-one">We do the training</span>
    <span class="line-two">and the state pays for it!</span>
  </h1>

  <div class="produce-wash" role="img" aria-label="Faint black and white photo of fresh produce"></div>

  <section class="panel training">
    <h2 class="panel-label">FREE TRAINING</h2>
    <div class="topic" style="left:104px">
      <svg width="61" height="61" viewBox="0 0 61 61"><circle cx="30.5" cy="30.5" r="29" fill="none" stroke="var(--ink)" stroke-width="2"/><circle cx="30.5" cy="30.5" r="25" fill="var(--ink)"/><path d="M22 30 h5 v12 h-5 z M28 31 l5-9 c2 0 3 2 2 5 h6 c2 0 3 2 2 4 l-2 8 c-1 2-2 3-4 3 h-9 z" fill="none" stroke="#fff" stroke-width="2" stroke-linejoin="round"/></svg>
      <p class="topic-name">Food Safety</p>
    </div>
    <div class="topic" style="left:264px">
      <svg width="61" height="61" viewBox="0 0 61 61"><circle cx="30.5" cy="30.5" r="29" fill="none" stroke="var(--ink)" stroke-width="2"/><circle cx="30.5" cy="30.5" r="25" fill="var(--ink)"/><rect x="18" y="17" width="25" height="20" fill="none" stroke="#fff" stroke-width="2"/><path d="M23 23 h15 M23 28 h15" stroke="#fff" stroke-width="1.6"/><circle cx="30.5" cy="40" r="5" fill="var(--ink)" stroke="#fff" stroke-width="2"/><path d="M27 44 l-2 6 M34 44 l2 6" stroke="#fff" stroke-width="2"/></svg>
      <p class="topic-name">FSMA</p>
    </div>
    <div class="topic" style="left:421px">
      <svg width="61" height="61" viewBox="0 0 61 61"><circle cx="30.5" cy="30.5" r="29" fill="none" stroke="var(--ink)" stroke-width="2"/><circle cx="30.5" cy="30.5" r="25" fill="var(--ink)"/><circle cx="30.5" cy="30.5" r="14" fill="none" stroke="#fff" stroke-width="2" stroke-dasharray="4 3"/><circle cx="30.5" cy="30.5" r="10" fill="none" stroke="#fff" stroke-width="2"/><circle cx="30.5" cy="30.5" r="4" fill="#fff"/></svg>
      <p class="topic-name">Production<br>Skills</p>
    </div>
    <div class="topic" style="left:608px">
      <svg width="61" height="61" viewBox="0 0 61 61"><circle cx="30.5" cy="30.5" r="29" fill="none" stroke="var(--ink)" stroke-width="2"/><circle cx="30.5" cy="30.5" r="25" fill="var(--ink)"/><circle cx="25" cy="22" r="5" fill="#fff"/><path d="M15 40 c0-8 5-11 10-11 c4 0 7 2 8 5 v6 z" fill="#fff"/><path d="M36 28 l7-3 l7 3 v6 c0 5-3 8-7 10 c-4-2-7-5-7-10 z" fill="#fff"/></svg>
      <p class="topic-name">Worker Safety</p>
    </div>
  </section>

  <section class="panel qualify">
    <h2 class="panel-label">HOW TO QUALIFY</h2>
    <ul class="criteria criteria-left">
      <li>Train <b>California</b> Workers Only</li>
      <li>Trainees must earn <b>$11/hour</b></li>
      <li><b>Full-time</b> workers only</li>
      <li>Employees must attend at least<br><b>8</b> Hours of training</li>
    </ul>
    <ul class="criteria criteria-right">
      <li>You must train <b>200 or more<br>employees</b></li>
      <li>Incumbent or <b>New-Hire workers</b><br>are eligible</li>
      <li><b>Seasonal</b> workers are eligible</li>
    </ul>
  </section>

  <div class="footer-rule"></div>
  <footer class="footer">
    <address class="address">
      <strong>Daniel Hartwell</strong><br>
      Keystone Learning Company, Inc.<br>
      1820 Harbor Crest Drive<br>
      Suite 310 Irvine, CA 92614
    </address>
    <div class="divider" style="left:260px"></div>
    <div class="contact" style="left:279px;top:27px">
      <svg width="20" height="20" viewBox="0 0 20 20"><circle cx="10" cy="10" r="8.5" fill="none" stroke="#fff" stroke-width="1.5"/><ellipse cx="10" cy="10" rx="4" ry="8.5" fill="none" stroke="#fff" stroke-width="1.3"/><path d="M1.5 10 h17 M3 5.5 h14 M3 14.5 h14" stroke="#fff" stroke-width="1.3"/></svg>
      <span>www.KLGCAL.com</span>
    </div>
    <div class="contact" style="left:279px;top:65px">
      <svg width="20" height="20" viewBox="0 0 20 20"><circle cx="10" cy="10" r="8.5" fill="none" stroke="#fff" stroke-width="1.5"/><ellipse cx="10" cy="10" rx="4" ry="8.5" fill="none" stroke="#fff" stroke-width="1.3"/><path d="M1.5 10 h17 M3 5.5 h14 M3 14.5 h14" stroke="#fff" stroke-width="1.3"/></svg>
      <span>www.KLGFoodSafety.com</span>
    </div>
    <div class="divider" style="left:504px"></div>
    <div class="contact contact-email" style="left:525px;top:24px">
      <svg width="25" height="18" viewBox="0 0 25 18"><rect x="1" y="1" width="23" height="16" fill="none" stroke="#fff" stroke-width="1.5"/><path d="M1 1 l11.5 9 l11.5-9 M1 17 l8-7 M24 17 l-8-7" fill="none" stroke="#fff" stroke-width="1.5"/></svg>
      <span>Dan.Hartwell@KLGCAL.com</span>
    </div>
    <div class="contact" style="left:529px;top:62px">
      <svg width="20" height="20" viewBox="0 0 24 24"><path d="M6.6 10.8c1.4 2.8 3.8 5.1 6.6 6.6l2.2-2.2c.3-.3.7-.4 1-.2 1.1.4 2.3.6 3.6.6.6 0 1 .4 1 1V20c0 .6-.4 1-1 1C10.6 21 3 13.4 3 4c0-.6.4-1 1-1h3.5c.6 0 1 .4 1 1 0 1.3.2 2.5.6 3.6.1.3 0 .7-.2 1z" fill="#fff"/></svg>
      <span>(949) 555-0142</span>
    </div>
  </footer>
</div>
</body>
</html>
```